Party signage for a Wedding in Tuscany, Italy. Fun, design project !

Design three different templates to be translated to different signage dimensions by event. Details of the theme, creative input, and dimensions are attached.
Updates

I completed the brief late and cut the time short for the designers.

Target Market(s)

25-45 years old European family

Font styles to use
Script

Requirements
Must have
• Three different designs to complement the mood boards are provided
Nice to have
• Mood boards are included in the attachment for inspiration

```html
<!DOCTYPE html>
<html lang="en">
<head>
<meta charset="utf-8">
<title>Tuscany Wedding Signage Templates</title>
<link rel="stylesheet" href="https://fonts.googleapis.com/css2?family=Great+Vibes&family=Parisienne&family=PT+Sans&display=swap">
<style>
  :root {
    --bg-top: #16201f;
    --bg-mid: #1f2d2f;
    --label: #0d0f10;
    --ink: #161414;
    --sage-band: #8d9775;
    --sage-panel: #d8d2d2;
    --sage-line: #eae6df;
    --rose-band: #e48b81;
    --rose-panel: #efcdc8;
    --rose-line: #f6ddd8;
    --sun: #e3d87b;
    --gate: #f56d1c;
    --leaf: #7f9c70;
    --paper: #ffffff;
    --sketch: #1b1b1b;
    --ornament-grey: #d9d9d9;
  }
  * { margin: 0; padding: 0; box-sizing: border-box; }
  html, body { width: 1200px; height: 1172px; overflow: hidden; }
  body {
    position: relative;
    background: radial-gradient(ellipse at 50% 45%, #22393c 0%, var(--bg-mid) 45%, var(--bg-top) 100%);
    font-family: "Parisienne", cursive;
    color: var(--ink);
  }
  .size-label {
    position: absolute;
    transform: translateX(-50%);
    font-family: "PT Sans", sans-serif;
    font-size: 25px;
    color: var(--label);
    white-space: nowrap;
  }
  .size-label.small { font-size: 16px; }
  .card { position: absolute; overflow: hidden; }
  .panel { position: absolute; }
  .title {
    position: absolute; left: 0; right: 0;
    text-align: center;
    font-family: "Great Vibes", cursive;
    line-height: 1.25;
  }
  .body-copy {
    position: absolute;
    text-align: center;
    font-size: 8px;
    line-height: 12.6px;
  }
  .art { position: absolute; border-radius: 4px; }

  /* striped menus */
  .card--sage { background: var(--sage-band); width: 219px; height: 287px; top: 84px; }
  .card--sage .panel {
    inset: 17px 18px;
    background: var(--sage-panel);
    outline: 1px solid var(--sage-line);
    outline-offset: 3px;
    border: 1px solid var(--sage-line);
  }
  .card--sage .art { background: #b4aeac; }
  .card--sage .body-copy { left: 42px; right: 42px; font-size: 7.4px; line-height: 11.2px; }
  .card--rose { background: var(--rose-band); width: 250px; height: 319px; top: 78px; }
  .card--rose .panel {
    inset: 19px 18px;
    background: var(--rose-panel);
    outline: 1px solid var(--rose-line);
    outline-offset: 3px;
    border: 1px solid var(--rose-line);
  }
  .card--rose .art { background: #d8aaa4; }
  .card--rose .body-copy { left: 50px; right: 44px; }

  /* garden gate bars */
  .card--gate { background: var(--sun); width: 254px; height: 317px; }
  .gate-frame { position: absolute; background: var(--gate); }
  .gate-frame--beam { left: 4px; top: 10px; width: 240px; height: 26px; border-radius: 3px; opacity: .9; }
  .gate-frame--post-left { left: 28px; top: 36px; width: 12px; height: 281px; }
  .gate-frame--post-right { left: 215px; top: 36px; width: 12px; height: 281px; }
  .card--gate .art { background: var(--leaf); opacity: .85; }
  .card--gate .title { font-size: 27px; }
  .card--gate .body-copy { left: 52px; right: 44px; }

  /* line-art cards */
  .card--paper { background: var(--paper); }
  .card--paper .art { background: var(--ornament-grey); }
  .card--paper .body-copy { left: 64px; right: 64px; }
  .sketch-frame { position: absolute; border: 1px solid var(--sketch); }
  .divider { position: absolute; left: 50%; transform: translateX(-50%); }
</style>
</head>
<body>

<!-- 7x9 striped set -->
<div class="size-label" style="left:291px; top:36px;">size- 7x9</div>

<div class="card card--sage" style="left:66px;">
  <div class="panel"></div>
  <div class="title" style="top:48px; font-size:25px;">Sweet Treats<br>Menu</div>
  <p class="body-copy" style="top:114px;">Lorem ipsum dolor sit amet, consectetuer adipiscing elit, sed diam nonummy nibh euismod tincidunt ut laoreet dolore magna aliquam erat volutpat. Ut wisi enim ad minim veniam, quis nostrud exerci tation ullamcorper suscipit lobortis nisl ut aliquip ex ea commodo consequat.</p>
  <div class="art" style="left:176px; top:180px; width:31px; height:89px;" role="img" aria-label="Line drawing of a cocktail glass with umbrella and lemon slice"></div>
</div>

<div class="card card--sage" style="left:300px;">
  <div class="panel"></div>
  <div class="title" style="top:60px; font-size:25px;">Mains Menu</div>
  <p class="body-copy" style="top:104px;">Lorem ipsum dolor sit amet, consectetuer adipiscing elit, sed diam nonummy nibh euismod tincidunt ut laoreet dolore magna aliquam erat volutpat. Ut wisi enim ad minim veniam, quis nostrud exerci tation ullamcorper suscipit lobortis nisl ut aliquip ex ea commodo consequat.</p>
  <div class="art" style="left:170px; top:186px; width:37px; height:85px;" role="img" aria-label="Line drawing of a goblet with lemon and straw"></div>
</div>

<!-- 8x10 striped set -->
<div class="size-label" style="left:873px; top:36px;">size- 8x10</div>

<div class="card card--rose" style="left:607px;">
  <div class="panel"></div>
  <div class="title" style="top:38px; font-size:29px;">Summer<br>Spritz Bar</div>
  <p class="body-copy" style="top:120px;">Lorem ipsum dolor sit amet, consectetuer adipiscing elit, sed diam nonummy nibh euismod tincidunt ut laoreet dolore magna aliquam erat volutpat. Ut wisi enim ad minim veniam, quis nostrud exerci tation ullamcorper suscipit lobortis nisl ut aliquip ex ea commodo consequat.</p>
  <div class="art" style="left:199px; top:211px; width:46px; height:87px;" role="img" aria-label="Line drawing of a martini glass with cherries and umbrella"></div>
</div>

<div class="card card--rose" style="left:878px;">
  <div class="panel"></div>
  <div class="title" style="top:62px; font-size:29px;">Side Menu</div>
  <p class="body-copy" style="top:113px;">Lorem ipsum dolor sit amet, consectetuer adipiscing elit, sed diam nonummy nibh euismod tincidunt ut laoreet dolore magna aliquam erat volutpat. Ut wisi enim ad minim veniam, quis nostrud exerci tation ullamcorper suscipit lobortis nisl ut aliquip ex ea commodo consequat.</p>
  <div class="art" style="left:186px; top:230px; width:46px; height:68px;" role="img" aria-label="Line drawing of a tumbler with ice, herbs and a straw"></div>
</div>

<!-- 8x10 garden gate set -->
<div class="size-label" style="left:313px; top:398px;">size- 8x10</div>

<div class="card card--gate" style="left:66px; top:455px;">
  <div class="gate-frame gate-frame--beam" role="img" aria-label="Hand-drawn orange pergola beam"></div>
  <div class="gate-frame gate-frame--post-left" role="img" aria-label="Hand-drawn orange pergola post"></div>
  <div class="gate-frame gate-frame--post-right" role="img" aria-label="Hand-drawn orange pergola post"></div>
  <div class="title" style="top:54px;">The Recovery<br>Bar</div>
  <p class="body-copy" style="top:136px;">Lorem ipsum dolor sit amet, consectetuer adipiscing elit, sed diam nonummy nibh euismod tincidunt ut laoreet dolore magna aliquam erat volutpat. Ut wisi enim ad minim veniam, quis nostrud exerci tation ullamcorper suscipit lobortis nisl ut aliquip ex ea commodo consequat.</p>
  <div class="art" style="left:80px; top:240px; width:100px; height:74px;" role="img" aria-label="Silhouettes of dancing guests and a cocktail"></div>
</div>

<div class="card card--gate" style="left:334px; top:455px;">
  <div class="gate-frame gate-frame--beam" role="img" aria-label="Hand-drawn orange pergola beam"></div>
  <div class="gate-frame gate-frame--post-left" role="img" aria-label="Hand-drawn orange pergola post"></div>
  <div class="gate-frame gate-frame--post-right" role="img" aria-label="Hand-drawn orange pergola post"></div>
  <div class="title" style="top:64px;">Munchie Bar</div>
  <p class="body-copy" style="top:136px;">Lorem ipsum dolor sit amet, consectetuer adipiscing elit, sed diam nonummy nibh euismod tincidunt ut laoreet dolore magna aliquam erat volutpat. Ut wisi enim ad minim veniam, quis nostrud exerci tation ullamcorper suscipit lobortis nisl ut aliquip ex ea commodo consequat.</p>
  <div class="art" style="left:90px; top:243px; width:70px; height:74px;" role="img" aria-label="Striped popcorn bucket illustration"></div>
</div>

<div class="card card--gate" style="left:70px; top:777px;">
  <div class="gate-frame gate-frame--beam" role="img" aria-label="Hand-drawn orange pergola beam"></div>
  <div class="gate-frame gate-frame--post-left" role="img" aria-label="Hand-drawn orange pergola post"></div>
  <div class="gate-frame gate-frame--post-right" role="img" aria-label="Hand-drawn orange pergola post"></div>
  <div class="title" style="top:66px;">Pizza Bar</div>
  <p class="body-copy" style="top:136px;">Lorem ipsum dolor sit amet, consectetuer adipiscing elit, sed diam nonummy nibh euismod tincidunt ut laoreet dolore magna aliquam erat volutpat. Ut wisi enim ad minim veniam, quis nostrud exerci tation ullamcorper suscipit lobortis nisl ut aliquip ex ea commodo consequat.</p>
  <div class="art" style="left:68px; top:236px; width:108px; height:81px; border-radius:54px 54px 0 0;" role="img" aria-label="Line illustration of a sliced pizza"></div>
</div>

<div class="card card--gate" style="left:332px; top:777px;">
  <div class="gate-frame gate-frame--beam" role="img" aria-label="Hand-drawn orange pergola beam"></div>
  <div class="gate-frame gate-frame--post-left" role="img" aria-label="Hand-drawn orange pergola post"></div>
  <div class="gate-frame gate-frame--post-right" role="img" aria-label="Hand-drawn orange pergola post"></div>
  <div class="title" style="top:64px;">Salad Bar</div>
  <p class="body-copy" style="top:136px;">Lorem ipsum dolor sit amet, consectetuer adipiscing elit, sed diam nonummy nibh euismod tincidunt ut laoreet dolore magna aliquam erat volutpat. Ut wisi enim ad minim veniam, quis nostrud exerci tation ullamcorper suscipit lobortis nisl ut aliquip ex ea commodo consequat.</p>
  <div class="art" style="left:80px; top:240px; width:80px; height:77px;" role="img" aria-label="Line illustration of a salad bowl with leaves"></div>
</div>

<!-- 8x10 line-art set -->
<div class="size-label" style="left:864px; top:412px;">size- 8x10</div>

<div class="card card--paper" style="left:615px; top:449px; width:250px; height:318px;">
  <div class="sketch-frame" style="inset:6px 8px 10px 6px;"></div>
  <div class="art" style="left:55px; top:5px; width:142px; height:23px;" role="img" aria-label="Floral line ornament"></div>
  <div class="title" style="top:38px; font-size:27px;">Libations</div>
  <svg class="divider" style="top:84px;" width="86" height="12" viewBox="0 0 86 12" aria-hidden="true">
    <path d="M2 6 Q22 10 43 6 Q64 10 84 6" fill="none" stroke="var(--sketch)" stroke-width="1.2"/>
    <path d="M43 9 C37 3 40 0 43 3 C46 0 49 3 43 9 Z" fill="var(--sketch)"/>
  </svg>
  <p class="body-copy" style="top:116px;">Lorem ipsum dolor sit amet, consectetuer adipiscing elit, sed diam nonummy nibh euismod tincidunt ut laoreet dolore magna aliquam erat volutpat. Ut wisi enim ad minim veniam, quis nostrud exerci tation ullamcorper suscipit lobortis nisl ut aliquip ex ea commodo consequat.</p>
  <div class="art" style="left:178px; top:205px; width:71px; height:93px;" role="img" aria-label="Flourish swirl ornament"></div>
  <div class="art" style="left:2px; top:197px; width:18px; height:52px;" role="img" aria-label="Leafy sprig ornament"></div>
  <div class="art" style="left:68px; top:302px; width:110px; height:12px;" role="img" aria-label="Floral line ornament"></div>
</div>

<div class="card card--paper" style="left:881px; top:449px; width:250px; height:318px;">
  <div class="art" style="left:4px; top:4px; width:72px; height:44px;" role="img" aria-label="Floral corner ornament"></div>
  <div class="art" style="left:176px; top:4px; width:70px; height:70px;" role="img" aria-label="Floral corner ornament with ring"></div>
  <div class="title" style="top:34px; font-size:27px;">Wine, Beer,<br>Spritz Bar</div>
  <svg class="divider" style="top:111px;" width="86" height="12" viewBox="0 0 86 12" aria-hidden="true">
    <path d="M2 6 Q22 10 43 6 Q64 10 84 6" fill="none" stroke="var(--sketch)" stroke-width="1.2"/>
    <path d="M43 9 C37 3 40 0 43 3 C46 0 49 3 43 9 Z" fill="var(--sketch)"/>
  </svg>
  <p class="body-copy" style="top:136px;">Lorem ipsum dolor sit amet, consectetuer adipiscing elit, sed diam nonummy nibh euismod tincidunt ut laoreet dolore magna aliquam erat volutpat. Ut wisi enim ad minim veniam, quis nostrud exerci tation ullamcorper suscipit lobortis nisl ut aliquip ex ea commodo consequat.</p>
  <div class="art" style="left:203px; top:180px; width:43px; height:135px;" role="img" aria-label="Vine ornament with two lovebirds"></div>
  <div class="art" style="left:4px; top:250px; width:60px; height:64px;" role="img" aria-label="Floral corner ornament with champagne glasses"></div>
</div>

<!-- small stationery -->
<div class="size-label small" style="left:1037px; top:822px;">size- 4x7</div>
<div class="card card--paper" style="left:979px; top:847px; width:124px; height:222px;">
  <div class="art" style="left:10px; top:6px; width:104px; height:16px;" role="img" aria-label="Floral line ornament"></div>
  <div class="title" style="top:34px; font-size:19px;">Menu/ Place<br>Cards</div>
  <span class="sketch-frame" style="left:6px; top:58px; width:0; height:130px; border-width:0 0 0 1px;"></span>
  <span class="sketch-frame" style="right:6px; top:70px; width:0; height:135px; border-width:0 0 0 1px;"></span>
  <p class="body-copy" style="left:22px; right:22px; top:91px; font-size:6.8px; line-height:11.3px;">Lorem ipsum dolor sit amet, consectetuer adipiscing elit, sed diam nonummy nibh euismod tincidunt ut laoreet dolore magna aliquam erat volutpat.</p>
  <div class="art" style="left:28px; top:206px; width:68px; height:10px;" role="img" aria-label="Floral line ornament"></div>
</div>

<div class="size-label small" style="left:903px; top:905px;">size- 4.5x4.5</div>
<div class="card card--paper" style="left:814px; top:932px; width:140px; height:142px;">
  <div class="art" style="left:16px; top:4px; width:108px; height:15px;" role="img" aria-label="Floral line ornament"></div>
  <div class="title" style="top:22px; font-size:25px; line-height:34px;">Table<br>Numbers</div>
  <div class="art" style="left:34px; top:124px; width:72px; height:9px;" role="img" aria-label="Floral line ornament"></div>
</div>

<div class="size-label small" style="left:719px; top:980px;">size- 4x2</div>
<div class="card card--paper" style="left:657px; top:1009px; width:124px; height:63px;">
  <div class="art" style="left:28px; top:2px; width:68px; height:11px;" role="img" aria-label="Floral line ornament"></div>
  <div class="title" style="top:16px; font-size:19px;">Escort Cards</div>
  <div class="art" style="left:28px; top:48px; width:68px; height:11px;" role="img" aria-label="Floral line ornament"></div>
</div>

</body>
</html>
```